business stationery

have a gorgeous logo that needs to be incorporated on stationery. Was hoping to do something on letterhead that was a paper that looked like "bark" from a tree or something that resembled the "woods." Soft paper with some very basic natural elements. Same thing for business cards. Think American lakeside cabin. Organic. Natural. Calm and welcoming but clear to read and understand. Wanted to use alot of black.

Target Market(s)

buyers of Conrad Bellweather home. Client that would have more than one home and in need of rare pieces and items to furnish an upmarket lakeside holiday cabin in the woods. Someone who treasures beautiful hand made items, organic foods and a real crackling fire but with money to burn in it!

Industry/Entity Type

Business

Requirements
Must have
• My logo
My business name
www.thornbydell.example
Natural almost raw effect paper
My ABN: 62 730 514 907 (to be placed in small writing at the bottom of card/letterhead)
Nice to have
• The website will consist of a cabin door that you "open" with a creak sound effect and then you go "inside" to look at the various rooms to start shopping. Want to bring that element of texture and warmth into the stationary also.
Should not have
• Anything modern or hard to read items

```html
<!DOCTYPE html>
<html lang="en">
<head>
<meta charset="utf-8">
<title>Thornby Dell — Business Stationery</title>
<link rel="stylesheet" href="https://fonts.googleapis.com/css2?family=Crimson+Text:wght@400;600&display=swap">
<style>
  :root {
    --backdrop: #2a1a12;
    --paper-light: #ece3d6;
    --paper-mid: #e2d6c5;
    --paper-dark: #d8cab7;
    --grain: rgba(150, 126, 98, 0.14);
    --grain-deep: rgba(130, 106, 80, 0.12);
    --ink: #1a1414;
    --ink-soft: #3a3230;
    --maple: #8e1b1b;
    --rule: #6d6660;
    --band: #0d0707;
  }
  * { box-sizing: border-box; margin: 0; padding: 0; }
  html, body {
    width: 1200px; height: 900px; overflow: hidden;
    background: var(--backdrop);
    font-family: "Crimson Text", Georgia, serif;
    color: var(--ink);
  }
  .raw-paper {
    background:
      radial-gradient(ellipse 18% 70% at 22% 40%, var(--grain-deep), transparent 70%),
      radial-gradient(ellipse 12% 55% at 58% 62%, var(--grain), transparent 70%),
      radial-gradient(ellipse 20% 80% at 84% 30%, var(--grain-deep), transparent 72%),
      repeating-linear-gradient(94deg, transparent 0 22px, var(--grain) 27px, transparent 33px, transparent 48px, var(--grain-deep) 52px, transparent 58px),
      linear-gradient(160deg, var(--paper-light) 0%, var(--paper-mid) 55%, var(--paper-dark) 100%);
  }
  .sheet {
    position: absolute;
    box-shadow: 2px 3px 8px rgba(0,0,0,0.55);
  }
  .brand {
    display: flex; align-items: center; gap: 7px;
    font-weight: 600; color: var(--ink); letter-spacing: 0.04em; line-height: 1;
    text-transform: uppercase; white-space: nowrap;
  }
  .brand-mark { background: var(--maple); flex: none; }
  .logo-block { display: inline-flex; flex-direction: column; }
  .byline { font-size: 6px; color: var(--maple); letter-spacing: 0.06em; text-transform: uppercase; text-align: right; margin-top: 3px; }
  .contact { color: var(--ink-soft); line-height: 1.3; }
  .abn { font-size: 7px; color: var(--ink-soft); }

  /* Letterhead */
  .letterhead { left: 44px; top: 44px; width: 532px; height: 752px; padding: 124px 0 0 32px; }
  .letterhead .brand { font-size: 31px; }
  .letterhead .brand-mark { width: 15px; height: 15px; }
  .letterhead .web { font-size: 11px; margin-top: 10px; }
  .letterhead .address { font-size: 11px; margin-top: 14px; }
  .letterhead .abn { margin-top: 6px; }

  /* Compliment slip */
  .slip { left: 84px; top: 290px; width: 528px; height: 250px; padding: 56px 0 0 17px; }
  .slip .brand { font-size: 21px; }
  .slip .brand-mark { width: 10px; height: 10px; }
  .slip .byline { font-size: 4.5px; }
  .slip .web { font-size: 7.5px; margin-top: 6px; }
  .slip .address { font-size: 7.5px; margin-top: 9px; }
  .slip .abn { font-size: 5px; margin-top: 3px; }

  /* Business card front */
  .card-front { left: 750px; top: 46px; width: 266px; height: 166px; }
  .card-front .band { position: absolute; left: 0; width: 100%; height: 28px; background: var(--band); }
  .card-front .band-top { top: 0; }
  .card-front .band-bottom { bottom: 0; }
  .card-front .logo-block { position: absolute; left: 0; right: 0; top: 86px; align-items: center; }
  .card-front .brand { font-size: 23px; gap: 6px; }
  .card-front .brand-mark { width: 11px; height: 11px; }
  .card-front .byline { font-size: 4.5px; align-self: flex-end; margin-right: 38px; }

  /* Business card back */
  .card-back { left: 750px; top: 224px; width: 266px; height: 162px; }
  .card-back .logo-block { position: absolute; left: 14px; top: 58px; width: 92px; }
  .card-back .brand { font-size: 15px; flex-direction: column; align-items: flex-start; gap: 4px; }
  .card-back .brand-mark { width: 10px; height: 10px; }
  .card-back .divider { position: absolute; left: 112px; top: 14px; width: 1px; height: 134px; background: var(--rule); }
  .card-back .details { position: absolute; right: 3px; top: 38px; width: 150px; text-align: right; font-size: 8.5px; line-height: 1.35; color: var(--ink-soft); }
  .card-back .details strong { font-weight: 600; color: var(--ink); }
  .card-back .web { margin-top: 10px; }
  .card-back .abn { font-size: 6px; margin-top: 10px; }

  /* Envelope back (open flap) */
  .envelope-back { left: 628px; top: 458px; width: 552px; height: 356px; box-shadow: none; }
  .envelope-back .envelope-body { position: absolute; left: 0; top: 82px; width: 552px; height: 274px; box-shadow: 2px 3px 8px rgba(0,0,0,0.55); }
  .envelope-back svg { position: absolute; inset: 0; }

  /* Envelope front */
  .envelope-front { left: 303px; top: 592px; width: 544px; height: 278px; padding: 48px 0 0 20px; }
  .envelope-front .brand { font-size: 19px; gap: 6px; }
  .envelope-front .brand-mark { width: 9px; height: 9px; }
  .envelope-front .byline { font-size: 4.5px; }
  .envelope-front .return-address { position: absolute; right: 12px; bottom: 10px; font-size: 7px; text-align: right; line-height: 1.3; color: var(--ink-soft); }
</style>
</head>
<body>
  <section class="sheet raw-paper letterhead">
    <div class="logo-block">
      <div class="brand"><span class="brand-mark"></span>Thornby Dell</div>
      <div class="byline">by Tessa Harlow</div>
    </div>
    <p class="contact web">www.thornbydell.example</p>
    <p class="contact address">4820 N. Alder Creek Rd.<br>Fenwick, IN 46099-0000<br>555/210-3381</p>
    <p class="abn">ABN 62 730 514 907</p>
  </section>

  <section class="sheet raw-paper slip">
    <div class="logo-block">
      <div class="brand"><span class="brand-mark"></span>Thornby Dell</div>
      <div class="byline">by Tessa Harlow</div>
    </div>
    <p class="contact web">www.thornbydell.example</p>
    <p class="contact address">4820 N. Alder Creek Rd.<br>Fenwick, IN 46099-0000<br>555/210-3381</p>
    <p class="abn">ABN 62 730 514 907</p>
  </section>

  <section class="sheet raw-paper card-front">
    <div class="band band-top"></div>
    <div class="logo-block">
      <div class="brand"><span class="brand-mark"></span>Thornby Dell</div>
      <div class="byline">by Tessa Harlow</div>
    </div>
    <div class="band band-bottom"></div>
  </section>

  <section class="sheet raw-paper card-back">
    <div class="logo-block">
      <div class="brand"><span class="brand-mark"></span><span>Thornby<br>Dell</span></div>
    </div>
    <div class="divider"></div>
    <div class="details">
      <p>Head Office; 18 Birchwood Lane<br>Glenmore, Sydney, Australia 2000</p>
      <p><strong>T: 0400 118 562</strong><br><strong>E Mail: (Tbc)</strong></p>
      <p class="web"><strong>www.thornbydell.example</strong></p>
      <p class="abn">ABN 62 730 514 907</p>
    </div>
  </section>

  <section class="sheet envelope-back" aria-label="Envelope back with open flap">
    <div class="envelope-body raw-paper"></div>
    <svg width="552" height="356" viewBox="0 0 552 356">
      <path d="M0 82 L12 38 Q20 26 40 24 L250 0 L300 0 L512 24 Q532 26 540 38 L552 82 Z" fill="#0d0707"/>
      <path d="M14 84 Q276 112 538 84" fill="none" stroke="#0d0707" stroke-width="14"/>
      <line x1="0" y1="82" x2="552" y2="82" stroke="#8a8078" stroke-width="1"/>
    </svg>
  </section>

  <section class="sheet raw-paper envelope-front">
    <div class="logo-block">
      <div class="brand"><span class="brand-mark"></span>Thornby Dell</div>
      <div class="byline">by Tessa Harlow</div>
    </div>
    <p class="return-address">18 Birchwood Lane, Glenmore<br>Sydney, Australia 2000</p>
  </section>
</body>
</html>
```